Web design - holistic filmmaker

I need a design for my new website.

I am a holistic filmmaker, ie I make films for healers, alternative practitioners, spiritual people and institutions that offer training in this field.

The design should be noble, bright, convey the feeling of space and expanse and have some particularly beautiful color accents.

The structure is: start page, offer, references, about me, imprint.

As an idea for the start page, I thought that either I could introduce myself as a filmmaker and my offer, or we could start right on the start page with the references, ie photos and links to already realized projects.

If you want more information or an exchange, I'd love to hear from you. At the moment I just don't know how to describe it better.

The winner will then be asked to design a logo.

Target Market(s)

healers, alternative practitioners, spiritual people and institutions that offer training in this field

Industry/Entity Type

Film production

Number of Pages Required

3 page

```html
<!DOCTYPE html>
<html lang="en">
<head>
<meta charset="utf-8">
<title>Elias Brandt – Holistic Filmmaker</title>
<link rel="stylesheet" href="https://fonts.googleapis.com/css2?family=Marcellus&family=Montserrat:wght@300;400;500;600;700&display=swap">
<style>
:root{
  --brown:#5a3b2e;
  --brown-dark:#4a2f24;
  --gold:#d6ad79;
  --gold-text:#c9a06a;
  --cream:#faf6f0;
  --ink:#3b2a22;
  --grey-head:#e6e1dc;
  --text:#4b4038;
  --black:#0d0d0d;
  --black-bar:#161616;
  --white:#ffffff;
}
*{margin:0;padding:0;box-sizing:border-box}
html,body{width:1200px;height:4338px;overflow:hidden;background:var(--white)}
body{font-family:"Montserrat",sans-serif;color:var(--text)}
.page{position:relative;width:1200px;height:4338px;overflow:hidden}
.abs{position:absolute}
.display{font-family:"Marcellus",serif;color:var(--brown);text-transform:uppercase;font-weight:400;line-height:1}
.subhead{font-family:"Montserrat",sans-serif;font-weight:400;text-transform:uppercase;color:var(--ink);line-height:1.45}
.copy{font-size:11px;line-height:1.75;color:var(--text);padding-left:12px;border-left:1px solid var(--brown)}
.btn{position:absolute;display:flex;align-items:center;justify-content:center;gap:8px;font-size:9px;font-weight:700;letter-spacing:2.5px;text-transform:uppercase}
.btn svg{width:16px;height:6px}
.btn-brown{background:var(--brown);color:var(--white);border-right:3px solid var(--gold)}
.btn-gold{background:var(--gold);color:var(--white);border-right:3px solid var(--brown)}
.btn-white{background:var(--white);color:var(--brown);border-right:3px solid var(--gold)}
.photo{position:absolute}
/* header */
.logo{left:138px;top:28px;font-family:"Marcellus",serif;font-size:34px;color:var(--brown);letter-spacing:1px}
.nav a{position:absolute;top:38px;font-size:10px;letter-spacing:.5px;color:var(--ink);text-decoration:none;text-transform:uppercase}
.nav a.active{font-weight:700}
.nav .underline{position:absolute;left:425px;top:80px;width:36px;height:4px;background:var(--brown)}
.nav-rule{left:426px;top:86px;width:651px;height:1px;background:#cfc7c1}
/* pricing */
.card{position:absolute;background:var(--white);text-align:center;box-shadow:0 10px 30px rgba(0,0,0,.06)}
.card-head{height:44px;background:var(--grey-head);display:flex;align-items:center;justify-content:center;font-family:"Marcellus",serif;font-size:16px;color:var(--brown)}
.price{font-family:"Marcellus",serif;font-size:25px;color:var(--brown);margin-top:38px}
.per{font-size:8px;font-weight:700;letter-spacing:.5px;color:var(--brown);margin-top:10px}
.features{list-style:none;margin-top:22px;font-size:8px;color:var(--text)}
.features li{height:29px}
.card .btn{left:37px;width:155px;height:47px}
.card.premium{background:var(--gold)}
.card.premium .card-head{background:var(--gold);color:var(--white);height:56px}
.card.premium .price,.card.premium .per,.card.premium .features{color:var(--white)}
.card.premium .price{font-size:33px;margin-top:20px}
/* footer */
.footer-nav a{position:absolute;top:4102px;font-size:12px;color:var(--white);text-decoration:none;text-transform:uppercase}
.contact-icon{position:absolute;width:38px;height:38px;border-radius:50%;background:var(--gold);display:flex;align-items:center;justify-content:center}
.contact-icon svg{width:16px;height:16px}
.contact-label{position:absolute;font-size:7px;font-weight:700;letter-spacing:2px;color:var(--white)}
.contact-value{position:absolute;font-size:11px;color:var(--white);line-height:1.7}
.social{position:absolute;top:4300px;width:22px;height:22px;border-radius:50%;background:var(--white)}
.play{position:absolute;width:70px;height:70px;border-radius:50%;background:rgba(255,255,255,.35);border:2px solid rgba(255,255,255,.8);display:flex;align-items:center;justify-content:center}
.play svg{width:22px;height:22px}
</style>
</head>
<body>
<div class="page">

  <!-- HERO -->
  <div class="photo" style="left:0;top:0;width:609px;height:670px;background:linear-gradient(135deg,#e9e6e2 0%,#a9a39d 45%,#3b3836 100%)" role="img" aria-label="Black and white portrait of the filmmaker smiling, hands near his face"></div>
  <div class="abs logo">ELIAS BRANDT</div>
  <nav class="nav">
    <a class="active" style="left:426px">Home</a>
    <a style="left:513px">Offer</a>
    <a style="left:604px">Refrences</a>
    <a style="left:724px">About me</a>
    <a style="left:837px">Imprint</a>
    <span class="underline"></span>
  </nav>
  <div class="btn btn-brown" style="left:948px;top:30px;width:118px;height:30px">Contact <svg viewBox="0 0 16 6"><path d="M0 3h15M12 0l3 3-3 3" stroke="currentColor" fill="none"/></svg></div>
  <div class="abs nav-rule"></div>

  <h1 class="abs display" style="left:535px;top:152px;font-size:42px;letter-spacing:1px">Movies for</h1>
  <div class="abs subhead" style="left:670px;top:204px;font-size:44px;line-height:1.15">Awakened<br>Ones</div>
  <p class="abs copy" style="left:677px;top:326px;width:278px">With simple means and without special effects, I accompany you on the way to portraying your essence. A documentary commercial film close to the people. Films for Awakened is aimed at all people and institutions whose striving for truthfulness is the driving force behind their actions</p>
  <div class="btn btn-gold" style="left:678px;top:493px;width:145px;height:30px">Get started <svg viewBox="0 0 16 6"><path d="M0 3h15M12 0l3 3-3 3" stroke="currentColor" fill="none"/></svg></div>

  <!-- ABOUT -->
  <div class="photo" style="left:816px;top:624px;width:384px;height:424px;background:linear-gradient(160deg,#6b4a2c 0%,#2a2220 45%,#b07a4a 100%)" role="img" aria-label="The filmmaker holding a professional video camera on his shoulder at night"></div>
  <h2 class="abs display" style="left:199px;top:757px;font-size:40px">About me</h2>
  <div class="abs subhead" style="left:300px;top:810px;font-size:29px;line-height:1.45">I am a holistic<br>filmmaker.</div>
  <div class="abs copy" style="left:197px;top:914px;width:560px;padding-left:12px">
    <p>My name is Elias and I do movies - with enthusiasm and wholeheartedly. I am a holistic filmmaker. At the end of the 1990s, I was faced with the question of whether I should go into alternative medicine or the film industry as a career. Professionally, I chose film at that time, but the spiritual and my passion for the so-called alternative healing methods have accompanied me almost as intensely ever since.</p>
    <p style="margin-top:20px">My cinematic path literally brought me from cable guy to cameraman, director and producer. It all started in 1995 as a camera assistant for the US news agency NBX. In the following years, I worked in various positions on numerous national and international television productions, cinema and documentary films, commercials and live productions.</p>
  </div>
  <div class="btn btn-brown" style="left:197px;top:1138px;width:162px;height:29px">Explore more <svg viewBox="0 0 16 6"><path d="M0 3h15M12 0l3 3-3 3" stroke="currentColor" fill="none"/></svg></div>

  <!-- PRODUCTION -->
  <div class="photo" style="left:0;top:1281px;width:884px;height:596px;background:linear-gradient(180deg,#f0d9b0 0%,#d99a4e 40%,#8a5a2a 75%,#4a3420 100%)" role="img" aria-label="Man standing on a mountain rock with arms spread wide in golden sunset light"></div>
  <div class="abs" style="left:609px;top:1200px;width:591px;height:468px;background:var(--brown)"></div>
  <h2 class="abs display" style="left:687px;top:1310px;font-size:40px;color:var(--gold);line-height:1.12">The production<br>of your film</h2>
  <div class="abs subhead" style="left:747px;top:1406px;font-size:30px;color:var(--white);line-height:1.4">Is always also a<br>journey to yourself.</div>
  <div class="btn btn-white" style="left:687px;top:1523px;width:152px;height:31px">Get started <svg viewBox="0 0 16 6"><path d="M0 3h15M12 0l3 3-3 3" stroke="currentColor" fill="none"/></svg></div>

  <!-- REFERENCES -->
  <h2 class="abs display" style="left:199px;top:2027px;font-size:40px">Refrences</h2>
  <div class="abs subhead" style="left:266px;top:2079px;font-size:29px">From my recent<br>projects</div>

  <div class="photo" style="left:609px;top:1991px;width:394px;height:276px;background:linear-gradient(135deg,#c9b8a6 0%,#8c6f5c 50%,#b23a5a 100%)" role="img" aria-label="Video still of a woman in a pink sweater speaking in a seminar room">
    <div class="play" style="left:162px;top:103px"><svg viewBox="0 0 22 22"><path d="M7 4l12 7-12 7z" fill="#fff"/></svg></div>
  </div>
  <div class="photo" style="left:197px;top:2217px;width:394px;height:277px;background:linear-gradient(135deg,#5c6b3c 0%,#8c8a7a 45%,#7a3a3a 100%)" role="img" aria-label="Video still of a healer treating a woman outdoors">
    <div class="play" style="left:162px;top:103px"><svg viewBox="0 0 22 22"><path d="M7 4l12 7-12 7z" fill="#fff"/></svg></div>
    <span class="abs" style="left:36px;top:230px;font-size:16px;color:var(--white)">Lorem Ipsum is simply dummy</span>
  </div>
  <div class="photo" style="left:609px;top:2286px;width:394px;height:277px;background:linear-gradient(160deg,#3d6fb5 0%,#8fb0d8 45%,#4a3a30 100%)" role="img" aria-label="Video still of a woman in a coat under blue sky">
    <div class="play" style="left:162px;top:103px"><svg viewBox="0 0 22 22"><path d="M7 4l12 7-12 7z" fill="#fff"/></svg></div>
  </div>
  <div class="photo" style="left:197px;top:2513px;width:394px;height:277px;background:linear-gradient(135deg,#7a8a5a 0%,#5a4a3a 55%,#2a2420 100%)" role="img" aria-label="Video still of a singer in a period costume beside a tree">
    <div class="play" style="left:162px;top:103px"><svg viewBox="0 0 22 22"><path d="M7 4l12 7-12 7z" fill="#fff"/></svg></div>
    <span class="abs" style="left:326px;top:20px;width:64px;height:64px;border-radius:50%;background:var(--white)"></span>
  </div>
  <svg class="abs" style="left:943px;top:2513px" width="100" height="100" viewBox="0 0 100 100" aria-label="Book me">
    <circle cx="50" cy="50" r="50" fill="#6a3a2c"/>
    <defs><path id="ring" d="M50 50m-34 0a34 34 0 1 1 68 0a34 34 0 1 1-68 0"/></defs>
    <text font-family="Montserrat,sans-serif" font-size="8" font-weight="700" letter-spacing="2" fill="#fff"><textPath href="#ring">BOOK ME · BOOK ME · BOOK ME ·</textPath></text>
    <path d="M42 58l16-16M46 42h12v12" stroke="#fff" stroke-width="1.6" fill="none"/>
  </svg>
  <p class="abs copy" style="left:658px;top:2645px;width:262px">As a full-service provider, I offer everything from one source, from consulting and conception to the finished film.</p>
  <div class="btn btn-gold" style="left:660px;top:2727px;width:146px;height:29px">Get started <svg viewBox="0 0 16 6"><path d="M0 3h15M12 0l3 3-3 3" stroke="currentColor" fill="none"/></svg></div>

  <!-- PRICING -->
  <section class="abs" style="left:0;top:2903px;width:1200px;height:749px;background:var(--cream)">
    <h2 class="abs display" style="left:0;top:92px;width:1200px;text-align:center;font-size:40px">As a full-service provider</h2>
    <div class="abs subhead" style="left:0;top:143px;width:1200px;text-align:center;font-size:29px">I offer everything from<br>one source</div>

    <div class="card" style="left:256px;top:256px;width:229px;height:370px">
      <div class="card-head">Basic Package</div>
      <div class="price">$49.00</div>
      <div class="per">PER MONTH</div>
      <ul class="features"><li>1 Hour Session</li><li>10 Digital Images</li><li>Online Gallery</li><li>1 Photographer</li></ul>
      <div class="btn btn-brown" style="top:296px;border:none">Purchase now</div>
    </div>
    <div class="card" style="left:714px;top:256px;width:229px;height:370px">
      <div class="card-head">Professional Package</div>
      <div class="price">$49.00</div>
      <div class="per">PER MONTH</div>
      <ul class="features"><li>3 Hour Session</li><li>30 Digital Images</li><li>Online Gallery</li><li>4 Photographer</li></ul>
      <div class="btn btn-brown" style="top:296px;border:none">Purchase now</div>
    </div>
    <div class="card premium" style="left:485px;top:243px;width:229px;height:403px">
      <div class="card-head">Premium Package</div>
      <div class="price">$49.00</div>
      <div class="per">PER MONTH</div>
      <ul class="features" style="margin-top:18px"><li style="height:39px">2 Hour Session</li><li style="height:39px">20 Digital Images</li><li style="height:39px">Online Gallery</li><li>2 Photographer</li></ul>
      <div class="btn btn-white" style="top:328px;border:none">Purchase now</div>
    </div>
  </section>

  <!-- NEWSLETTER -->
  <section class="abs" style="left:0;top:3652px;width:1200px;height:274px;background:var(--gold)">
    <h2 class="abs display" style="left:198px;top:60px;font-size:40px;line-height:1.42">Stay in the know!<br><span style="color:var(--white)">For our latest<br>updates</span></h2>
    <p class="abs" style="left:660px;top:72px;width:342px;text-align:right;font-size:12px;line-height:1.9;color:var(--white)">Documentary advertising films that are<br>close to the people</p>
    <div class="abs" style="left:660px;top:133px;width:343px;height:30px;background:var(--white);font-size:8px;letter-spacing:1px;color:#9a918a;padding:11px 0 0 30px">EMAIL</div>
    <div class="btn btn-brown" style="left:831px;top:177px;width:172px;height:29px;border-right:3px solid var(--white)">Subscribe now <svg viewBox="0 0 16 6"><path d="M0 3h15M12 0l3 3-3 3" stroke="currentColor" fill="none"/></svg></div>
  </section>

  <!-- FOOTER -->
  <footer class="abs" style="left:0;top:3926px;width:1200px;height:412px;background:var(--black)">
    <div class="abs" style="left:198px;top:108px;width:210px;height:1px;background:var(--gold)"></div>
    <div class="abs" style="left:793px;top:108px;width:210px;height:1px;background:var(--gold)"></div>
    <div class="abs" style="left:0;top:83px;width:1200px;text-align:center;font-family:'Marcellus',serif;font-size:48px;color:var(--white);letter-spacing:1px">ELIAS BRANDT</div>
  </footer>
  <nav class="footer-nav">
    <a style="left:316px">Home</a><a style="left:401px">Offer</a><a style="left:489px">Refrences</a><a style="left:611px">About me</a><a style="left:724px">Imprint</a><a style="left:823px">Contact</a>
  </nav>
  <div class="contact-icon" style="left:302px;top:4163px"><svg viewBox="0 0 16 16"><rect x="2" y="4" width="12" height="9" rx="1" fill="#5a3b2e"/><path d="M2 5l6 4 6-4" stroke="#d6ad79" fill="none"/></svg></div>
  <div class="contact-label" style="left:356px;top:4170px">EMAIL:</div>
  <div class="contact-value" style="left:356px;top:4182px">info@eliasbrandt.com</div>
  <div class="contact-icon" style="left:530px;top:4163px"><svg viewBox="0 0 16 16"><path d="M4 2l2 3-1.5 1.5a8 8 0 0 0 5 5L11 10l3 2-1.5 2.5C7 14 2 9 1.5 3.5z" fill="#5a3b2e"/></svg></div>
  <div class="contact-label" style="left:583px;top:4170px">PHONE:</div>
  <div class="contact-value" style="left:583px;top:4182px">0000-555-123</div>
  <div class="contact-icon" style="left:752px;top:4163px"><svg viewBox="0 0 16 16"><path d="M8 1a5 5 0 0 0-5 5c0 4 5 9 5 9s5-5 5-9a5 5 0 0 0-5-5z" fill="#5a3b2e"/><circle cx="8" cy="6" r="1.8" fill="#d6ad79"/></svg></div>
  <div class="contact-label" style="left:805px;top:4167px">ADDRESS:</div>
  <div class="contact-value" style="left:805px;top:4179px;width:160px;font-size:10px">Lorem Ipsum is simply dummy text of the printing</div>

  <div class="abs" style="left:0;top:4283px;width:1200px;height:55px;background:var(--black-bar)"></div>
  <div class="abs" style="left:197px;top:4307px;font-size:8px;color:var(--white);letter-spacing:.3px">COPYRIGHT © 2023 ELIAS BRANDT. ALL RIGHT RESERVED</div>
  <span class="social" style="left:886px"></span>
  <span class="social" style="left:932px"></span>
  <span class="social" style="left:977px"></span>
</div>
</body>
</html>
```